Larkfield civic consultancy needs a business card design

Business card should represent civil engineering infrastructure projects such as roads, bridges, tunnels, rail, rail, pipelines, structures and resource infrastructure

```html
<!DOCTYPE html>
<html lang="en">
<head>
<meta charset="utf-8">
<title>Larkfield civic consultancy – business card</title>
<link rel="stylesheet" href="https://fonts.googleapis.com/css2?family=Oswald:wght@300;400;500&display=swap">
<style>
  :root {
    --stage: #2f2b29;
    --navy: #2b2a80;
    --navy-deep: #23226e;
    --stone: #c9cdc0;
    --gold: #c9a227;
    --gold-dark: #5a4718;
    --white: #ffffff;
    --ink: #111111;
    --cream: #f6efc9;
    --cream-soft: #e6e0c4;
    --charcoal-mid: #484b45;
    --charcoal-edge: #070a07;
  }
  * { margin: 0; padding: 0; box-sizing: border-box; }
  html, body { width: 1000px; height: 1200px; overflow: hidden; background: var(--stage); }
  .canvas { position: relative; width: 1000px; height: 1200px; font-family: "Oswald", sans-serif; }

  .card { position: absolute; width: 740px; height: 457px; overflow: hidden; }
  .card--front { left: 132px; top: 119px; background: linear-gradient(90deg, var(--navy-deep) 0%, var(--navy) 40%, var(--navy-deep) 70%); }
  .card--back { left: 117px; top: 665px; background: radial-gradient(ellipse 55% 70% at 50% 45%, var(--charcoal-mid) 0%, #2a2d28 55%, var(--charcoal-edge) 100%); }

  .card__sweep { position: absolute; inset: 0; }

  .brand-name { position: absolute; font-weight: 400; letter-spacing: 1px; line-height: 1; transform: translateX(-50%); }
  .card--front .brand-name { left: 518px; top: 98px; font-size: 66px; color: var(--ink); }
  .card--back .brand-name { left: 370px; top: 110px; font-size: 70px; color: var(--cream); }

  .brand-mark { position: absolute; border-radius: 50%; background: var(--gold); transform: translateX(-50%); }
  .card--front .brand-mark { left: 518px; top: 190px; width: 110px; height: 110px; }
  .card--back .brand-mark { left: 370px; top: 205px; width: 100px; height: 100px; }

  .brand-floor { position: absolute; left: 370px; top: 305px; width: 165px; height: 18px; transform: translateX(-50%); border-radius: 50%; background: radial-gradient(ellipse at center, rgba(200,190,150,.55), rgba(200,190,150,0) 70%); }

  .web-email { position: absolute; white-space: nowrap; transform: translateX(-50%); }
  .card--front .web-email { left: 520px; top: 370px; font-size: 19px; font-weight: 500; color: var(--ink); }
  .card--back .web-email { left: 370px; top: 335px; font-size: 21px; font-weight: 300; color: var(--cream-soft); }

  .contact-list { position: absolute; left: 44px; top: 339px; list-style: none; color: #e9e9f3; font-weight: 300; font-size: 18px; }
  .contact-list li { display: flex; align-items: center; gap: 8px; height: 32px; }
  .contact-list svg { width: 16px; height: 14px; fill: #f2c318; }
</style>
</head>
<body>
<main class="canvas">

  <section class="card card--front" aria-label="Card front">
    <svg class="card__sweep" viewBox="0 0 740 457" preserveAspectRatio="none" aria-hidden="true">
      <defs>
        <linearGradient id="goldBand" x1="0" y1="0" x2="0" y2="1">
          <stop offset="0" stop-color="var(--gold-dark)"/>
          <stop offset="0.6" stop-color="#b8901f"/>
          <stop offset="1" stop-color="#f0cf3a"/>
        </linearGradient>
      </defs>
      <path d="M468 0 Q 270 200 335 457 L740 457 L740 0 Z" fill="var(--white)"/>
      <path d="M548 0 Q 300 180 340 457 L740 457 L740 0 Z" fill="url(#goldBand)"/>
      <path d="M562 0 Q 318 190 345 457 L740 457 L740 0 Z" fill="var(--stone)"/>
    </svg>

    <div class="brand-name">LCC</div>
    <div class="brand-mark" aria-hidden="true"></div>
    <div class="web-email">daniel.hale@larkfieldcivic.com.au</div>

    <ul class="contact-list">
      <li>
        <svg viewBox="0 0 16 12" aria-hidden="true"><path d="M0 0h16v12H0z M0 0l8 6 8-6" /><path d="M0 0l8 6 8-6" fill="none" stroke="var(--navy)" stroke-width="1.4"/></svg>
        daniel.j.hale@mailbay.com
      </li>
      <li>
        <svg viewBox="0 0 16 16" aria-hidden="true"><path d="M3 1l3 3-1.5 2c1 2 3 4 5 5l2-1.5 3 3-2 2C7 14 2 9 1 3z"/></svg>
        +61400555127
      </li>
    </ul>
  </section>

  <section class="card card--back" aria-label="Card back">
    <div class="brand-name">LCC</div>
    <div class="brand-floor" aria-hidden="true"></div>
    <div class="brand-mark" aria-hidden="true"></div>
    <div class="web-email">daniel.hale@larkfieldcivic.com.au</div>
  </section>

</main>
</body>
</html>
```